Four Key Ledger Blueprint Presentation

I would like a flyer to hand out to participants at the speeches that we give. We are a CPA firm that specializes in entrepreneurs and realtors. We would like a flyer that looks crisp and clean, that integrates our logo and our company colors (shades of blue & gold). We would like the wording to be as laid out in the attached documents, but design is up to you. We would like a picture to go along with each point and are open to ideas. The flyer should be one page, preferably just the front.

Colors
3176b5
fee18a

Requirements
Must have
• Our logo and the wording supplied.
• A picture to go along with each topic.
Nice to have
• Images that pop, clean look, professional.
Should not have
• Look messy.

```html
<!DOCTYPE html>
<html lang="en">
<head>
<meta charset="utf-8">
<title>Steadfast Ledger – Presentation Agenda Flyer</title>
<link rel="stylesheet" href="https://fonts.googleapis.com/css2?family=Arimo:wght@400;700&family=Carlito:wght@400;700&display=swap">
<style>
  :root {
    --brand-blue: #3176b5;
    --brand-gold: #fee18a;
    --deep-navy: #14325a;
    --paper: #ffffff;
    --ink: #1d1d1d;
    --backdrop: #e9ecf0;
    --footer-text: #a9c4ec;
  }
  * { margin: 0; padding: 0; box-sizing: border-box; }
  html, body { width: 1200px; height: 1200px; overflow: hidden; }
  body {
    background: var(--backdrop);
    font-family: "Carlito", "Calibri", sans-serif;
    color: var(--ink);
    position: relative;
  }
  .flyer {
    position: absolute;
    left: 300px; top: 20px;
    width: 600px; height: 1160px;
    background: var(--paper);
    overflow: hidden;
    box-shadow: 0 4px 18px rgba(0,0,0,0.15);
  }
  .band { position: absolute; left: 0; width: 600px; }
  .band--top { top: 0; height: 300px; }
  .band--bottom { top: 990px; height: 170px; }

  .brand {
    position: absolute; top: 40px; left: 0; width: 600px;
    text-align: center;
  }
  .brand__name {
    font-family: "Arimo", sans-serif; font-weight: 700;
    font-size: 46px; color: var(--brand-gold); letter-spacing: 1px;
  }
  .brand__tagline {
    font-family: "Arimo", sans-serif; font-size: 14px;
    color: var(--deep-navy); margin-top: 6px;
  }
  .agenda-title {
    position: absolute; top: 148px; left: 20px; width: 560px;
    font-family: "Arimo", sans-serif; font-weight: 700;
    font-size: 23px; line-height: 1.25; color: var(--brand-gold);
    text-align: center;
  }

  .step {
    position: absolute; width: 180px;
    font-size: 14px; line-height: 1.22;
  }
  .step__num {
    font-family: "Arimo", sans-serif; font-weight: 700;
    font-size: 20px; color: var(--brand-gold);
  }
  .photo {
    position: absolute; width: 86px; height: 86px; border-radius: 50%;
  }

  .slogan {
    position: absolute; left: 40px; width: 520px; top: 1040px;
    font-family: "Arimo", sans-serif; font-size: 21px; line-height: 1.2;
    color: var(--brand-gold); text-align: center;
  }
  .contact {
    position: absolute; left: 20px; width: 560px; top: 1096px;
    font-size: 12px; line-height: 1.3; color: var(--footer-text);
    text-align: center; font-style: normal;
  }
  .contact__row { display: flex; justify-content: space-between; }
</style>
</head>
<body>
  <main class="flyer">
    <svg class="band band--top" viewBox="0 0 600 300" aria-hidden="true">
      <path d="M0 0 H600 V252 Q300 318 0 232 Z" fill="var(--brand-gold)"/>
      <path d="M0 0 H600 V228 Q300 292 0 208 Z" fill="var(--brand-blue)"/>
    </svg>

    <header class="brand">
      <div class="brand__name">Steadfast Ledger</div>
      <div class="brand__tagline">A Professional Accounting Corporation</div>
    </header>
    <h1 class="agenda-title">Four Key Ledger Blueprint Presentation Agenda:</h1>

    <section class="step" style="left:20px; top:280px;">
      <span class="step__num">1.</span> We will first show you how to eliminate much of your self-employment tax on your return by converting your business into an S Corporation. A business owner making over $120,000 per year can save about $12,000 per year by doing this.
    </section>
    <div class="photo" role="img" aria-label="S Corporation emblem" style="left:65px; top:442px; background:radial-gradient(circle,#f4f5f7,#d8dbe0);"></div>
    <section class="step" style="left:20px; top:542px;">
      <span class="step__num">2.</span> We will show you how to get tax free income from your corporation by renting you home to the corporation for the board meetings. Many of our clients are getting up to $21,000 in tax free income which could put $8,400 cash into your pocket.
    </section>
    <div class="photo" role="img" aria-label="Board meeting around a conference table" style="left:65px; top:712px; background:radial-gradient(circle,#c98a5a,#6b4a33);"></div>

    <section class="step" style="left:212px; top:298px;">
      <span class="step__num">3.</span> We will show you the easiest way to track your expenses so that the only thing you will have to do to have rock solid books is to take a picture of the receipt and throw it away. It doesn't get any better than that.
    </section>
    <div class="photo" role="img" aria-label="Hands using a calculator with receipts" style="left:257px; top:475px; background:radial-gradient(circle,#f2f2f2,#b9bcc2);"></div>
    <section class="step" style="left:212px; top:575px;">
      <span class="step__num">4.</span> Next, we show you the importance of tax planning and why it is critical to meet with your CPA before the end of the year and not just when you do your tax preparation.
    </section>
    <div class="photo" role="img" aria-label="Magnifying glass and calculator on tax forms" style="left:257px; top:705px; background:radial-gradient(circle,#dfe8f3,#6f8fb5);"></div>
    <section class="step" style="left:212px; top:805px;">
      <span class="step__num">5.</span> We will show you how to hire your children and get $7,500 per child tax free. This will save you $3,000 per child in income tax reduction.
    </section>
    <div class="photo" role="img" aria-label="Surprised child holding cash" style="left:257px; top:900px; background:radial-gradient(circle,#e9c39c,#8f8a5e);"></div>

    <section class="step" style="left:405px; top:350px;">
      <span class="step__num">6.</span> We will discuss how to make your child's college education tax deductible. With college cost spiraling out of control this is a biggie. Most of our clients have a savings of about $12,000 per year of college.
    </section>
    <div class="photo" role="img" aria-label="Piggy bank in a graduation cap on cash" style="left:450px; top:522px; background:radial-gradient(circle,#f6d3df,#9aa582);"></div>
    <section class="step" style="left:405px; top:622px;">
      <span class="step__num">7.</span> Our grand finale is to show you how to use, not one, but two corporations to get a several hundred thousand dollar tax deferral, get an interest free loan from the government and use that money to grow your business and your wealth.
    </section>
    <div class="photo" role="img" aria-label="Alarm clock among falling money" style="left:450px; top:800px; background:radial-gradient(circle,#e9eef5,#8da2bd);"></div>

    <svg class="band band--bottom" viewBox="0 0 600 170" aria-hidden="true">
      <path d="M0 45 Q300 -5 600 45 V170 H0 Z" fill="var(--brand-gold)"/>
      <path d="M0 65 Q300 15 600 65 V170 H0 Z" fill="var(--brand-blue)"/>
    </svg>
    <footer>
      <p class="slogan">If they drive by with a machine gun you don't have to stand up.</p>
      <address class="contact">
        <div>Steadfast Ledger, A Professional Accounting Corporation</div>
        <div>820 Orchard Ave, Ste. B, Fairmont, CA 95012</div>
        <div>Phone: 555-014-2280 &nbsp;&nbsp; Fax: 555-014-2291</div>
        <div class="contact__row">
          <span>dana@steadfastledgercpa.com</span>
          <span>owen@steadfastledgercpa.com</span>
          <span>www.steadfastledgercpa.com</span>
        </div>
      </address>
    </footer>
  </main>
</body>
</html>
```